Brightmoor Notes To Do List

I am looking to design a new "Study To Do List" for High School students (Ages 15 - 18) . This will be printed as an A4 notepad and so should only be a single A4 page.

The Design will need to be professional and look semi-serious but also be appealing to High school students (Ages 15 - 18) and should NOT be gender specific.

I have attached a word document outlining the structure of the page. The space provided should be large enough that people can write in it comfortably.

The notepad will most likely be printed in black and white but I'm also looking at coloured options - colours should be kept to a minimum.

This will be printed professionally and should also include a 3mm bleed.

The design should also include the business logo (included in the word document)

Target Market(s)

High School students (Ages 15 - 18). Both genders

Industry/Entity Type

Education

Font styles to use
Serif
Sans Serif

Requirements
Must have
• Please see the word document attached.
Should not have
• Too much colour

```html
<!DOCTYPE html>
<html lang="en">
<head>
<meta charset="utf-8">
<title>Brightmoor Notes – Study To Do List</title>
<link rel="stylesheet" href="https://fonts.googleapis.com/css2?family=Lato:wght@400;700&display=swap">
<style>
  :root {
    --navy: #1f364a;
    --orange: #f47a20;
    --orange-row-a: #fde1d2;
    --orange-row-b: #fdf0ea;
    --grey-row-a: #e9eaec;
    --grey-row-b: #f3f4f5;
    --paper: #ffffff;
    --backdrop: #ececec;
    --ink: #1f2a33;
  }
  * { box-sizing: border-box; margin: 0; padding: 0; }
  html, body { width: 1200px; height: 1200px; overflow: hidden; }
  body { background: var(--backdrop); font-family: "Lato", sans-serif; color: var(--ink); position: relative; }

  .sheet {
    position: absolute; left: 190px; top: 20px;
    width: 728px; height: 1030px;
    background: var(--paper);
    transform: scale(1.126); transform-origin: 0 0;
    font-size: 14px;
  }
  .top-rule { position: absolute; left: 0; top: 0; width: 100%; height: 6px; background: var(--navy); }

  .brand {
    position: absolute; left: 0; width: 100%; top: 60px;
    display: flex; justify-content: center; align-items: center; gap: 8px;
    font-size: 22px; font-weight: 700; color: var(--navy);
  }
  .brand-dot { width: 16px; height: 16px; border-radius: 50%; background: var(--orange); }

  .date { position: absolute; left: 519px; top: 107px; font-size: 14px; }
  .date span { display: inline-block; width: 124px; border-bottom: 1px dotted var(--ink); margin-left: 3px; }

  .tab {
    position: absolute; left: 44px; height: 17px; padding-left: 7px;
    color: #fff; font-size: 14px; line-height: 17px;
    clip-path: polygon(0 0, calc(100% - 16px) 0, 100% 100%, 0 100%);
  }
  .tab--orange { background: var(--orange); }
  .tab--navy { background: var(--navy); }

  .block { position: absolute; left: 44px; width: 641px; display: grid; gap: 2px 2px; padding: 1px 1px; background: var(--paper); }
  .block > div { line-height: 1; display: flex; align-items: center; padding-left: 6px; }

  .revision { top: 137px; height: 90px; border: 1px solid var(--orange); grid-template-columns: 24px 293px 22px 1fr; grid-template-rows: repeat(4, 1fr); }
  .revision > div { color: var(--orange); }
  .revision .a { background: var(--orange-row-a); }
  .revision .b { background: var(--orange-row-b); }

  .homework { top: 256px; height: 284px; border: 2px solid var(--navy); grid-template-columns: 75px 1fr; grid-template-rows: repeat(12, 1fr); }
  .assessments { top: 568px; height: 284px; border: 2px solid var(--navy); grid-template-columns: 99px 215px 62px 1fr; grid-template-rows: repeat(12, 1fr); padding-left: 4px; }
  .a { background: var(--grey-row-a); }
  .b { background: var(--grey-row-b); }
  .label-cell { background: transparent !important; }
  .assessments .span { grid-column: 2 / 5; }

  .lists { position: absolute; left: 44px; top: 870px; width: 641px; border-collapse: collapse; table-layout: fixed; }
  .lists th { background: var(--navy); color: #fff; font-weight: 400; height: 22px; border: 1px solid var(--navy); }
  .lists td { height: 23px; border: 1px solid var(--navy); padding-left: 6px; }
  .lists .gap { border-left: 1px solid #fff; }

  .footer { position: absolute; left: 0; bottom: 0; width: 100%; height: 27px; background: var(--navy); }
  .footer-web {
    position: absolute; right: 0; top: 0; height: 27px; width: 253px;
    background: var(--orange); color: #fff; font-size: 14px; line-height: 27px;
    padding-left: 30px; clip-path: polygon(18px 0, 100% 0, 100% 100%, 0 100%);
  }
</style>
</head>
<body>
<main class="sheet">
  <div class="top-rule"></div>

  <div class="brand"><span class="brand-dot"></span>Brightmoor Notes</div>
  <div class="date">Date:<span></span></div>

  <div class="tab tab--orange" style="top:120px;width:97px">REVISION</div>
  <section class="block revision">
    <div class="a">1</div><div class="a"></div><div class="a">5</div><div class="a"></div>
    <div class="b">2</div><div class="b"></div><div class="b">6</div><div class="b"></div>
    <div class="a">3</div><div class="a"></div><div class="a">7</div><div class="a"></div>
    <div class="b">4</div><div class="b"></div><div class="b">8</div><div class="b"></div>
  </section>

  <div class="tab tab--navy" style="top:240px;width:127px">HOMEWORK</div>
  <section class="block homework">
    <div class="a label-cell">Subject</div><div class="a"></div>
    <div class="b label-cell">Task</div><div class="b"></div>
    <div class="a label-cell">Subject</div><div class="a"></div>
    <div class="b label-cell">Task</div><div class="b"></div>
    <div class="a label-cell">Subject</div><div class="a"></div>
    <div class="b label-cell">Task</div><div class="b"></div>
    <div class="a label-cell">Subject</div><div class="a"></div>
    <div class="b label-cell">Task</div><div class="b"></div>
    <div class="a label-cell">Subject</div><div class="a"></div>
    <div class="b label-cell">Task</div><div class="b"></div>
    <div class="a label-cell">Subject</div><div class="a"></div>
    <div class="b label-cell">Task</div><div class="b"></div>
  </section>

  <div class="tab tab--navy" style="top:552px;width:135px;padding-left:13px">ASSESSMENTS</div>
  <section class="block assessments">
    <div class="a">Assessment</div><div class="a"></div><div class="a">Due</div><div class="a"></div>
    <div class="b">Element</div><div class="b"></div><div class="b">Due</div><div class="b"></div>
    <div class="a">Assessment</div><div class="a"></div><div class="a">Due</div><div class="a"></div>
    <div class="b">Element</div><div class="b"></div><div class="b">Due</div><div class="b"></div>
    <div class="a">Assessment</div><div class="a"></div><div class="a">Due</div><div class="a"></div>
    <div class="b">Element</div><div class="b"></div><div class="b">Due</div><div class="b"></div>
    <div class="a">Assessment</div><div class="a"></div><div class="a">Due</div><div class="a"></div>
    <div class="b">Element</div><div class="b"></div><div class="b">Due</div><div class="b"></div>
    <div class="a">Assessment</div><div class="a"></div><div class="a">Due</div><div class="a"></div>
    <div class="b">Element</div><div class="b"></div><div class="b">Due</div><div class="b"></div>
    <div class="a">Assessment</div><div class="a"></div><div class="a">Due</div><div class="a"></div>
    <div class="b">Element</div><div class="b span"></div>
  </section>

  <table class="lists">
    <colgroup>
      <col style="width:23px"><col style="width:123px"><col style="width:23px"><col style="width:115px">
      <col style="width:25px"><col>
    </colgroup>
    <thead>
      <tr><th colspan="4">NOTES</th><th class="gap"></th><th class="gap">PRACTICE</th></tr>
    </thead>
    <tbody>
      <tr><td>1</td><td></td><td>5</td><td></td><td>1</td><td></td></tr>
      <tr><td>2</td><td></td><td>6</td><td></td><td>2</td><td></td></tr>
      <tr><td>3</td><td></td><td>7</td><td></td><td>3</td><td></td></tr>
      <tr><td>4</td><td></td><td>8</td><td></td><td>4</td><td></td></tr>
    </tbody>
  </table>

  <footer class="footer">
    <div class="footer-web">brightmoornotes.com.au</div>
  </footer>
</main>
</body>
</html>
```